Brill's Jewelers website (www.brillsjewelers-example.com)

We are in need of a web storefront for a retail Jewelry store.
www.brillsjewelers-example.com
https://www.facebook.com/Brills-Jewelers-Palm-Vista-740315928461257/

Brill's Jewelers is located in Coral Gables, Florida. The store has been family owned and operated since 1958. Their focus customers are high-income families that care about quality over the brand name. They mostly sell fashion jewelry and diamonds up to 8 carats. We are looking for a simple minimalistic site that their customers can view their inventory and purchase items online.

Competitors websites:
https://www.orvinjewelers-example.com/
http://www.pelvaro-example.com/
http://truecutjewelers-example.com/

Pages:
-Home (with message bulletin)
-Jewelry
We would be able to create the subpages ie Rings, Bracelets, Earrings, Necklaces, Estate, Watches, Men's, Children's
-Services
We would need sub pages ie Appraisals, Consignment, Repairs
-About us
-Contact

Target Market(s)

Local wealthy families

Coding

Number of Pages Required

Font styles to use
Serif

Requirements
Must have
• -An E-commerce site customers can buy jewelry online.
-An easy process internally to add new items to the site
-Colors are Black and White or Black and Gold
Nice to have
• I would like to stay away from face shots of random models in stock photos. I want the jewelry pieces as the focus, not models.

```html
<!DOCTYPE html>
<html lang="en">
<head>
<meta charset="utf-8">
<title>About Us – Brill's Jewelers</title>
<link href="https://fonts.googleapis.com/css2?family=Poppins:wght@400;500;600;700&family=Roboto:wght@400;500;700&display=swap" rel="stylesheet">
<style>
:root{
  --black:#111111;
  --ink:#1a1a1a;
  --white:#ffffff;
  --gold:#b8975a;
  --gold-soft:#c6a86c;
  --band:#e8e9ee;
  --muted:#3a3a3a;
  --footer-text:#d6d6d6;
}
*{margin:0;padding:0;box-sizing:border-box}
html,body{width:1200px;height:2346px;overflow:hidden}
body{position:relative;background:var(--white);font-family:'Roboto',sans-serif;color:var(--ink)}
.abs{position:absolute}

/* header */
.site-header{position:absolute;left:0;top:0;width:1200px;height:143px;background:var(--black);color:var(--white)}
.header-phone{position:absolute;left:88px;top:40px;display:flex;align-items:center;gap:8px;font-family:'Poppins',sans-serif;font-size:16px;font-weight:500}
.brand{position:absolute;left:500px;top:30px;width:200px;text-align:center;font-family:'Poppins',sans-serif;color:var(--white)}
.brand-name{font-size:28px;font-weight:700;letter-spacing:1px;line-height:1}
.brand-tag{font-size:9px;letter-spacing:1px;margin-top:4px}
.header-icons{position:absolute;right:88px;top:42px;display:flex;gap:16px}
.cart-count{position:absolute;right:-6px;top:-8px;width:15px;height:15px;border-radius:50%;background:var(--gold);color:var(--white);font-size:9px;text-align:center;line-height:15px}
.header-rule{position:absolute;left:88px;top:95px;width:1024px;height:1px;background:#2e2e2e}
.main-nav{position:absolute;left:0;top:108px;width:1200px;display:flex;justify-content:center;gap:36px;font-family:'Poppins',sans-serif;font-size:16px}
.main-nav a{color:var(--white);text-decoration:none}
.main-nav a.active{color:var(--gold)}

/* page title */
.page-title{position:absolute;left:0;top:143px;width:1200px;height:194px;background:var(--band);text-align:center}
.page-title h1{font-family:'Poppins',sans-serif;font-weight:700;font-size:44px;margin-top:64px;line-height:1}
.breadcrumb{font-family:'Poppins',sans-serif;font-size:16px;margin-top:12px}

/* history */
.history-photo{position:absolute;left:87px;top:428px;width:468px;height:332px;background:linear-gradient(135deg,#3a2c18 0%,#8a7448 45%,#5b4a30 100%)}
.history-copy{position:absolute;left:627px;top:510px;width:486px}
.section-head{font-family:'Roboto',sans-serif;font-weight:700;font-size:42px;line-height:1;color:var(--black)}
.history-copy p{margin-top:16px;font-size:15.5px;line-height:25px;color:var(--muted)}

/* staff */
.staff-title{position:absolute;left:0;top:840px;width:1200px;text-align:center}
.staff-card{position:absolute;top:904px;width:246px;height:303px;background:var(--white);box-shadow:0 10px 30px rgba(120,135,160,.16);text-align:center}
.avatar{width:148px;height:148px;border-radius:50%;margin:42px auto 0;border:10px solid #f2eee8;background:linear-gradient(160deg,#8c7f74,#4a4440)}
.staff-name{font-family:'Poppins',sans-serif;font-weight:500;font-size:21px;margin-top:14px;line-height:1.2}
.staff-role{font-family:'Poppins',sans-serif;font-size:16px;margin-top:2px}

/* community */
.community{position:absolute;left:0;top:1299px;width:1200px;height:438px;background:linear-gradient(120deg,#6e6358 0%,#4a3f36 40%,#2c231d 70%,#5d534b 100%);text-align:center}
.community h2{font-family:'Roboto',sans-serif;font-weight:700;font-size:56px;color:var(--white);margin-top:177px;line-height:1}
.btn-gold{display:inline-block;margin-top:12px;width:174px;height:45px;line-height:45px;background:var(--gold-soft);color:var(--white);font-family:'Roboto',sans-serif;font-weight:500;font-size:17px;text-decoration:none}

/* newsletter */
.newsletter{position:absolute;left:0;top:1737px;width:1200px;height:144px;background:linear-gradient(90deg,#c7a96c,#bfa066 60%,#c9ad74)}
.newsletter h3{position:absolute;left:88px;top:46px;font-family:'Poppins',sans-serif;font-weight:700;font-size:36px;color:var(--white);line-height:1}
.newsletter .sub{position:absolute;left:89px;top:86px;font-family:'Poppins',sans-serif;font-size:21px;color:var(--white)}
.email-field{position:absolute;left:650px;top:49px;width:405px;height:55px;background:var(--white);padding-left:20px;line-height:55px;font-size:16px;color:#333}
.email-send{position:absolute;left:1055px;top:49px;width:57px;height:55px;background:var(--black);display:flex;align-items:center;justify-content:center}

/* footer */
.site-footer{position:absolute;left:0;top:1881px;width:1200px;height:465px;background:#000;color:var(--footer-text)}
.footer-brand{position:absolute;left:86px;top:160px;width:220px;text-align:center;color:var(--white);font-family:'Roboto',sans-serif}
.footer-brand .brand-name{font-size:40px;font-weight:700;line-height:1}
.footer-brand .brand-tag{font-size:13px;letter-spacing:1.5px;margin-top:6px;border-top:1px solid var(--white);padding-top:4px}
.socials{position:absolute;left:128px;top:247px;display:flex;gap:6px}
.socials span{width:29px;height:29px;border-radius:50%;background:#1f1f1f;display:block}
.footer-col{position:absolute;top:100px}
.footer-col h4{font-family:'Poppins',sans-serif;font-weight:700;font-size:21px;color:var(--white);line-height:1;margin-bottom:16px}
.footer-col li{list-style:none;font-size:16px;line-height:29.4px}
.contact-item{display:flex;align-items:center;gap:6px;font-weight:700;color:var(--white)}
.contact-val{padding-left:18px}
.footer-rule{position:absolute;left:88px;top:400px;width:1024px;height:1px;background:#2b2b2b}
.copyright{position:absolute;left:89px;top:424px;font-family:'Roboto',sans-serif;font-weight:500;font-size:15px;color:var(--white)}
.pay-cards{position:absolute;left:959px;top:418px;display:flex;gap:6px}
.pay-cards span{width:46px;height:29px;border-radius:4px;background:#f2f2f2;display:block}
.pay-cards span.blue{background:#2a3fb8}
.to-top{position:absolute;left:1126px;top:385px;width:34px;height:34px;border-radius:50%;background:var(--gold);display:flex;align-items:center;justify-content:center}
</style>
</head>
<body>

<header class="site-header">
  <div class="header-phone">
    <svg width="16" height="16" viewBox="0 0 24 24"><path fill="#b8975a" d="M6.6 10.8a15.1 15.1 0 0 0 6.6 6.6l2.2-2.2c.3-.3.7-.4 1-.2 1.1.4 2.3.6 3.6.6.6 0 1 .4 1 1V20c0 .6-.4 1-1 1A17 17 0 0 1 3 4c0-.6.4-1 1-1h3.5c.6 0 1 .4 1 1 0 1.3.2 2.5.6 3.6.1.3 0 .7-.2 1z"/></svg>
    (305)555-0182
  </div>
  <div class="brand">
    <div class="brand-name">BRILL'S</div>
    <div class="brand-tag">YOUR HOMETOWN JEWELER</div>
  </div>
  <div class="header-icons">
    <svg width="20" height="20" viewBox="0 0 24 24" fill="none" stroke="#fff" stroke-width="1.6"><circle cx="12" cy="8" r="4.5"/><path d="M3.5 21c1-4.5 4.5-7 8.5-7s7.5 2.5 8.5 7"/></svg>
    <svg width="20" height="20" viewBox="0 0 24 24" fill="none" stroke="#fff" stroke-width="2.4"><circle cx="10.5" cy="10.5" r="6.5"/><path d="M15.5 15.5l5 5"/></svg>
    <span style="position:relative;display:block">
      <svg width="20" height="20" viewBox="0 0 24 24" fill="none" stroke="#fff" stroke-width="1.6"><path d="M4 8h16l-1.5 13h-13z"/><path d="M8.5 8V6a3.5 3.5 0 0 1 7 0v2"/></svg>
      <span class="cart-count">0</span>
    </span>
  </div>
  <div class="header-rule"></div>
  <nav class="main-nav">
    <a href="#">Home</a>
    <a href="#" class="active">About Us</a>
    <a href="#">Jewelry</a>
    <a href="#">Diamonds</a>
    <a href="#">Services</a>
    <a href="#">Contact</a>
  </nav>
</header>

<section class="page-title">
  <h1>ABOUT US</h1>
  <div class="breadcrumb">Home / About Us</div>
</section>

<div class="history-photo" role="img" aria-label="Storefront of Brill's Jewelers at night with lit display cases and customers at the entrance"></div>
<section class="history-copy">
  <h2 class="section-head">HISTORY</h2>
  <p>Lorem Ipsum is simply dummy text of the printing and typesetting industry. Lorem Ipsum has been the industry's standard dummy text ever since the 1500s, when an unknown printer took a galley of type and scrambled it to make a type specimen book. It has survived not only five centuries, but also the leap.</p>
</section>

<div class="staff-title"><h2 class="section-head">STAFF</h2></div>
<div class="staff-card" style="left:88px">
  <div class="avatar" role="img" aria-label="Portrait photo of staff member"></div>
  <div class="staff-name">John Smith</div><div class="staff-role">Manager</div>
</div>
<div class="staff-card" style="left:348px">
  <div class="avatar" role="img" aria-label="Portrait photo of staff member"></div>
  <div class="staff-name">John Smith</div><div class="staff-role">Manager</div>
</div>
<div class="staff-card" style="left:606px">
  <div class="avatar" role="img" aria-label="Portrait photo of staff member" style="background:linear-gradient(160deg,#e6cdb0,#b89a84)"></div>
  <div class="staff-name">John Smith</div><div class="staff-role">Manager</div>
</div>
<div class="staff-card" style="left:865px">
  <div class="avatar" role="img" aria-label="Portrait photo of staff member" style="background:linear-gradient(160deg,#8a6a60,#c23a7a)"></div>
  <div class="staff-name">John Smith</div><div class="staff-role">Manager</div>
</div>

<section class="community" role="img" aria-label="Store interior with glass jewelry display cases">
  <h2>COMMUNITY SUPPORT</h2>
  <a href="#" class="btn-gold">CONTACT NOW</a>
</section>

<section class="newsletter">
  <h3>NEWSLETTER</h3>
  <div class="sub">Subscribe to our newsletter</div>
  <div class="email-field">Email Address</div>
  <div class="email-send">
    <svg width="20" height="20" viewBox="0 0 24 24"><path fill="#fff" d="M22 2 2 10.5l7 2.5 2.5 7L22 2zM9.5 13.5 18 6l-6.5 9z"/></svg>
  </div>
</section>

<footer class="site-footer">
  <div class="footer-brand">
    <div class="brand-name">BRILL'S</div>
    <div class="brand-tag">YOUR HOMETOWN JEWELER</div>
  </div>
  <div class="socials"><span></span><span></span><span></span><span></span></div>

  <div class="footer-col" style="left:378px">
    <h4>USEFUL LINLS</h4>
    <ul><li>- Home</li><li>- About Us</li><li>- Jewelry</li><li>- Diamonds</li><li>- Services</li><li>- Contact</li></ul>
  </div>
  <div class="footer-col" style="left:613px">
    <h4>JEWELRY</h4>
    <ul><li>- Diamond</li><li>- Colored</li><li>- Pearls</li><li>- Estate</li><li>- Watches</li><li>- Brands</li></ul>
  </div>
  <div class="footer-col" style="left:804px">
    <h4>CONTACT US</h4>
    <ul>
      <li class="contact-item"><svg width="12" height="12" viewBox="0 0 24 24"><path fill="#b8975a" d="M12 2a7 7 0 0 0-7 7c0 5 7 13 7 13s7-8 7-13a7 7 0 0 0-7-7zm0 9.5A2.5 2.5 0 1 1 12 6.5a2.5 2.5 0 0 1 0 5z"/></svg>Email</li>
      <li class="contact-val">hello@brillsjewelers-example.com</li>
      <li class="contact-item"><svg width="12" height="12" viewBox="0 0 24 24"><path fill="#b8975a" d="M6.6 10.8a15.1 15.1 0 0 0 6.6 6.6l2.2-2.2c.3-.3.7-.4 1-.2 1.1.4 2.3.6 3.6.6.6 0 1 .4 1 1V20c0 .6-.4 1-1 1A17 17 0 0 1 3 4c0-.6.4-1 1-1h3.5c.6 0 1 .4 1 1 0 1.3.2 2.5.6 3.6.1.3 0 .7-.2 1z"/></svg>Phone</li>
      <li class="contact-val">(305)555-0182</li>
      <li class="contact-item"><svg width="12" height="12" viewBox="0 0 24 24"><path fill="#b8975a" d="M12 2a7 7 0 0 0-7 7c0 5 7 13 7 13s7-8 7-13a7 7 0 0 0-7-7zm0 9.5A2.5 2.5 0 1 1 12 6.5a2.5 2.5 0 0 1 0 5z"/></svg>Address</li>
      <li class="contact-val">418 Harbor Lane, Palm Vista, FL 33100</li>
    </ul>
  </div>

  <div class="to-top">
    <svg width="10" height="10" viewBox="0 0 24 24" fill="none" stroke="#fff" stroke-width="3"><path d="M5 15l7-7 7 7"/></svg>
  </div>
  <div class="footer-rule"></div>
  <div class="copyright">COPYRIGHT © 2020 | ALL RIGHTS RESRVED</div>
  <div class="pay-cards"><span></span><span class="blue"></span><span></span></div>
</footer>

</body>
</html>
```